Kolvane Business Card

Require a business card for KolVane. KolVane is an aircraft engineering consultancy company.
Company is used for end of leases inspections, pre purchase inspections,asset inspections

Industry/Entity Type

Business

Contact Information for Business Card

KolVane Limited
Rhys Palgrave
rhys@kolvane.example
64 (0)215580392

Requirements
Must have
• Aircraft silhouette in background

```html
<!DOCTYPE html>
<html lang="en">
<head>
<meta charset="utf-8">
<title>KolVane Business Card</title>
<link rel="stylesheet" href="https://fonts.googleapis.com/css2?family=Roboto+Slab:wght@300;400;800&display=block">
<style>
  :root {
    --card-bg: #ffffff;
    --ink: #333333;
    --brand-green: #46b94c;
    --brand-green-mid: #5cc262;
    --brand-green-fade: rgba(70, 185, 76, 0);
  }
  html, body {
    margin: 0;
    padding: 0;
    width: 1200px;
    height: 686px;
    overflow: hidden;
    background: var(--card-bg);
  }
  .card {
    position: relative;
    width: 1200px;
    height: 686px;
    overflow: hidden;
    background: var(--card-bg);
    font-family: "Roboto Slab", "Rockwell", "Arvo", serif;
    color: var(--ink);
  }
  .aircraft-silhouette {
    position: absolute;
    left: -120px;
    top: 250px;
    width: 780px;
    height: 230px;
    border-radius: 115px;
    transform: rotate(-58deg);
    transform-origin: center;
    background: linear-gradient(to bottom,
      var(--brand-green-fade) 0%,
      var(--brand-green-mid) 22%,
      var(--brand-green) 50%,
      var(--brand-green-mid) 78%,
      var(--brand-green-fade) 100%);
  }
  .company-name {
    position: absolute;
    right: 59px;
    top: 98px;
    margin: 0;
    font-size: 134px;
    font-weight: 800;
    line-height: 1;
    letter-spacing: -2px;
    color: var(--ink);
  }
  .person-name {
    position: absolute;
    right: 60px;
    top: 334px;
    margin: 0;
    font-size: 60px;
    font-weight: 300;
    line-height: 1;
    text-transform: uppercase;
    color: var(--ink);
  }
  .divider {
    position: absolute;
    left: 432px;
    right: 0;
    top: 418px;
    height: 3px;
    background: var(--brand-green);
  }
  .contact-list {
    position: absolute;
    right: 60px;
    top: 442px;
    margin: 0;
    padding: 0;
    list-style: none;
    text-align: right;
    font-size: 46px;
    font-weight: 300;
    line-height: 68px;
    color: var(--ink);
  }
</style>
</head>
<body>
  <main class="card">
    <div class="aircraft-silhouette" role="img" aria-label="Green aircraft silhouette seen from below, flying diagonally up across the left side of the card"></div>
    <h1 class="company-name">KolVane</h1>
    <p class="person-name">Rhys Palgrave</p>
    <div class="divider"></div>
    <ul class="contact-list">
      <li class="contact-company">KolVane Limited</li>
      <li class="contact-email">rhys@kolvane.example</li>
      <li class="contact-phone">64 (0)215-580-392</li>
    </ul>
  </main>
</body>
</html>
```